Christmas Collection Candle Label Design

Looking to update our existing Christmas Candle Collection labels. Labels should reflect the overall feel of our brand- www.kelvabrite.ca
Want to include some color elements. Holiday colors added into design but more muted/ earthy tones not vibrant colors . Metallic elements and line art botanical illustration. Fonts should be more align to brand
Scents
Winter Lantern
Frost Berry
Amber and Fig
Belle Étoile

```html
<!DOCTYPE html>
<html lang="en">
<head>
<meta charset="utf-8">
<title>Winter Lantern – Candle Label</title>
<link href="https://fonts.googleapis.com/css2?family=Cormorant+Garamond:wght@400;500;600&family=Great+Vibes&display=swap" rel="stylesheet">
<style>
  :root {
    --backdrop: #d6d6d4;
    --blush-light: #f6ebe7;
    --blush-mid: #ecd8d2;
    --blush-deep: #e2c7c0;
    --pine-dark: #1f3d38;
    --pine-mid: #2f6a4f;
    --pine-light: #5f9a6e;
    --ink: #1d3a3a;
    --band-text: #e9ddd6;
  }
  * { box-sizing: border-box; margin: 0; padding: 0; }
  html, body { width: 702px; height: 1200px; overflow: hidden; }
  body {
    background: var(--backdrop);
    font-family: "Cormorant Garamond", Georgia, serif;
    position: relative;
  }
  .label {
    position: absolute;
    left: 31px;
    top: 280px;
    width: 640px;
    height: 640px;
    background: radial-gradient(ellipse at 50% 45%, var(--blush-light) 0%, var(--blush-mid) 60%, var(--blush-deep) 100%);
    overflow: hidden;
    box-shadow: 0 2px 6px rgba(0,0,0,0.12);
  }
  .foliage {
    position: absolute;
    left: 0;
    width: 100%;
  }
  .foliage--top {
    top: 0;
    height: 140px;
    background: linear-gradient(180deg, var(--pine-dark) 0%, var(--pine-mid) 45%, rgba(95,154,110,0.35) 80%, rgba(95,154,110,0) 100%);
  }
  .foliage--bottom {
    bottom: 62px;
    height: 120px;
    background: linear-gradient(0deg, var(--pine-dark) 0%, var(--pine-mid) 40%, rgba(95,154,110,0.35) 78%, rgba(95,154,110,0) 100%);
  }
  .claim {
    position: absolute;
    top: 168px;
    width: 100%;
    text-align: center;
    color: var(--ink);
    font-weight: 600;
    font-size: 17px;
    letter-spacing: 2.5px;
    line-height: 1.35;
  }
  .scent-name {
    position: absolute;
    top: 222px;
    width: 100%;
    text-align: center;
    color: var(--ink);
  }
  .scent-name__main {
    display: block;
    font-weight: 500;
    font-size: 74px;
    letter-spacing: 4px;
    line-height: 1;
  }
  .scent-name__script {
    display: block;
    font-family: "Great Vibes", cursive;
    font-size: 76px;
    line-height: 1;
    margin-top: 2px;
  }
  .divider {
    position: absolute;
    top: 395px;
    left: 215px;
    width: 210px;
    height: 1px;
    background: var(--ink);
  }
  .notes {
    position: absolute;
    top: 408px;
    width: 100%;
    text-align: center;
    color: var(--ink);
    font-weight: 600;
    font-size: 16px;
    letter-spacing: 3px;
  }
  .info-band {
    position: absolute;
    left: 0;
    bottom: 0;
    width: 100%;
    height: 62px;
    background: var(--pine-dark);
    display: flex;
    align-items: center;
    justify-content: space-around;
    color: var(--band-text);
    font-size: 18px;
    font-weight: 500;
    letter-spacing: 0.5px;
  }
  .info-band__sep {
    width: 1px;
    height: 24px;
    background: var(--band-text);
  }
</style>
</head>
<body>
  <section class="label">
    <div class="foliage foliage--top" role="img" aria-label="Line-art evergreen and palm fronds in pine greens along the top edge"></div>

    <p class="claim">MADE WITH<br>PLANT BASED BOTANICAL</p>

    <h1 class="scent-name">
      <span class="scent-name__main">WINTER</span>
      <span class="scent-name__script">Lantern</span>
    </h1>

    <div class="divider"></div>
    <p class="notes">TUBEROSE • GARDENIA • PATCHOULI</p>

    <div class="foliage foliage--bottom" role="img" aria-label="Line-art evergreen and palm fronds in pine greens along the bottom edge"></div>

    <footer class="info-band">
      <span>Net WT. 10oz/283g</span>
      <span class="info-band__sep"></span>
      <span>Made in Canada</span>
      <span class="info-band__sep"></span>
      <span>Kelva Brite</span>
    </footer>
  </section>
</body>
</html>
```